Brenmoor Group needs a business card

I would like the card to be simple but modern and elegant.
I like black and white.
or black and gold.
we are a private finance lender and also are involved in property and property developments.

please look at the business card photos i provided i would like B.G only one one side and all the other details on the other side use fonts that tie in with my theme.

Industry/Entity Type

Finance

Contact Information for Business Card

Brenmoor Group (B.G) Callum Brenmoor M: 0418396152 E: callumbren@quivomail.com

Font styles to use
Other font styles liked:
• Use fonts that would reflect our business

Colors
000000
ffffff

Requirements
Must have
• one side of details
• other side has either B.G or Brenmoor Group like in the photos provided

```html
<!DOCTYPE html>
<html lang="en">
<head>
<meta charset="utf-8">
<title>Brenmoor Group – Business Card</title>
<link href="https://fonts.googleapis.com/css2?family=Open+Sans:wght@700&family=Noto+Serif:wght@400&display=swap" rel="stylesheet">
<style>
  :root {
    --page: #ffffff;
    --card-dark: #232525;
    --card-light: #f7f7f7;
    --gold: #d2b47a;
    --ink: #1c1a1a;
    --ink-soft: #3a3a3a;
    --monogram-faint: #ebebeb;
    --shadow: rgba(60, 55, 70, 0.55);
  }
  html, body {
    margin: 0;
    padding: 0;
    width: 806px;
    height: 1200px;
    overflow: hidden;
    background: var(--page);
  }
  .sheet {
    position: relative;
    width: 806px;
    height: 1200px;
  }
  .card {
    position: absolute;
    overflow: hidden;
    box-shadow: 4px 5px 6px var(--shadow);
  }
  .card--front {
    left: 81px;
    top: 97px;
    width: 629px;
    height: 408px;
    background: var(--card-dark);
  }
  .card--back {
    left: 81px;
    top: 690px;
    width: 625px;
    height: 402px;
    background: var(--card-light);
  }
  .monogram {
    font-family: "Open Sans", sans-serif;
    font-weight: 700;
    line-height: 1;
    margin: 0;
    position: absolute;
    letter-spacing: -2px;
  }
  .card--front .monogram {
    color: var(--gold);
    font-size: 164px;
    left: 0;
    right: 0;
    top: 92px;
    text-align: center;
  }
  .card--back .monogram {
    color: var(--monogram-faint);
    font-size: 218px;
    left: 306px;
    top: 5px;
    white-space: nowrap;
  }
  .details {
    position: absolute;
    left: 50px;
    top: 242px;
  }
  .details__name {
    font-family: "Open Sans", sans-serif;
    font-weight: 700;
    font-size: 26px;
    color: var(--ink);
    margin: 0 0 6px;
    line-height: 1.2;
  }
  .details__line {
    font-family: "Noto Serif", serif;
    font-size: 17.5px;
    color: var(--ink-soft);
    margin: 0;
    line-height: 24px;
  }
</style>
</head>
<body>
  <main class="sheet">
    <section class="card card--front" aria-label="Card front">
      <p class="monogram">B.G</p>
    </section>

    <section class="card card--back" aria-label="Card back">
      <p class="monogram" aria-hidden="true">B.G</p>
      <div class="details">
        <h1 class="details__name">Callum Brenmoor</h1>
        <p class="details__line">Brenmoor Group (B.G)</p>
        <p class="details__line">m: 0418396152</p>
        <p class="details__line">e: callumbren@quivomail.com</p>
      </div>
    </section>
  </main>
</body>
</html>
```